Startup photography business has a new logo, now we need business cards

Design a business card for the two partners of our business.
Our business Brisk Pelican has a new logo and we need to design a business card to showcase it and us.
Our colours of blue and orange are punchy and vivid, but how can we make the most of it on our card?

It should have our name Brisk Pelican
name of partner
phone number
email
website

Industry/Entity Type

Professional Photography

Contact Information for Business Card

Tom Ashworth
+61 400 55 61 72
tom@briskpelican.com.au
briskpelican.com.au

second card
Neil Porter
+61 400 918 263
neil@briskpelican.com.au
briskpelican.com.au

Colors
f37122
f68d4c
33a6d7
0592cd

Requirements
Must have
• one version of our logo, we have included options
• Name
• phone number
• email
• website
Nice to have
• instagram briskpelicanmedia
• twitter briskpelicanmedia
• facebook briskpelicanmedia

```html
<!DOCTYPE html>
<html lang="en">
<head>
<meta charset="utf-8">
<title>Brisk Pelican – Business Card</title>
<link rel="stylesheet" href="https://fonts.googleapis.com/css2?family=Tinos:ital,wght@0,700;1,700&family=Crimson+Pro:wght@600&display=swap">
<style>
  :root {
    --orange: #f37122;
    --orange-light: #f68d4c;
    --blue: #33a6d7;
    --blue-deep: #0592cd;
    --blue-dark: #0a78c4;
    --blue-pale: #6ccaee;
    --white: #ffffff;
    --ink: #3a3a3a;
    --icon-tile: #1f6fae;
  }
  * { margin: 0; padding: 0; box-sizing: border-box; }
  html, body { width: 1007px; height: 1200px; overflow: hidden; background: var(--white); }
  .card-sheet { position: relative; width: 1007px; height: 1200px; }
  .card-face { position: absolute; left: 0; width: 1007px; overflow: hidden; }
  .card-face--front { top: 0; height: 601px; }
  .card-face--back { top: 601px; height: 599px; }
  .card-face svg.backdrop { position: absolute; inset: 0; width: 100%; height: 100%; }

  .brand-mark { position: absolute; left: 52px; top: 22px; width: 290px; text-align: center; }
  .brand-mark__dot { display: block; width: 110px; height: 110px; margin: 0 auto 10px; border-radius: 50%; background: var(--orange); }
  .brand-mark__name { font-family: "Tinos", serif; font-weight: 700; font-size: 36px; color: var(--orange); letter-spacing: 1px; text-transform: uppercase; white-space: nowrap; }

  .contact { position: absolute; left: 571px; top: 388px; font-family: "Tinos", serif; font-style: italic; font-weight: 700; font-size: 35px; line-height: 48px; color: var(--ink); }

  .social { position: absolute; left: 188px; list-style: none; }
  .social__item { position: absolute; left: 0; display: flex; align-items: center; white-space: nowrap; }
  .social__tile { width: 108px; height: 108px; border-radius: 12px; background: var(--icon-tile); flex: none; }
  .social__handle { font-family: "Crimson Pro", serif; font-weight: 600; font-size: 34px; color: var(--white); margin-left: 26px; }
</style>
</head>
<body>
<main class="card-sheet">

  <section class="card-face card-face--front">
    <svg class="backdrop" viewBox="0 0 1007 601" aria-hidden="true">
      <defs>
        <linearGradient id="front-sky" x1="0" y1="1" x2="0.8" y2="0">
          <stop offset="0" stop-color="var(--blue-dark)"/>
          <stop offset="0.55" stop-color="var(--blue)"/>
          <stop offset="1" stop-color="var(--blue-pale)"/>
        </linearGradient>
      </defs>
      <rect width="1007" height="601" fill="url(#front-sky)"/>
      <ellipse cx="1170" cy="320" rx="420" ry="560" fill="var(--orange-light)"/>
      <ellipse cx="1210" cy="320" rx="390" ry="560" fill="var(--orange)"/>
      <circle cx="20" cy="-50" r="410" fill="var(--white)"/>
    </svg>

    <div class="brand-mark">
      <span class="brand-mark__dot"></span>
      <div class="brand-mark__name">Brisk Pelican</div>
    </div>

    <address class="contact">
      <div class="contact__name">Neil Porter</div>
      <div class="contact__phone">+61 400 918 263</div>
      <div class="contact__email">neil@briskpelican.com.au</div>
      <div class="contact__web">briskpelican.com.au</div>
    </address>
  </section>

  <section class="card-face card-face--back">
    <svg class="backdrop" viewBox="0 0 1007 599" aria-hidden="true">
      <defs>
        <linearGradient id="back-sky" x1="0" y1="0" x2="1" y2="1">
          <stop offset="0" stop-color="var(--blue-pale)"/>
          <stop offset="0.5" stop-color="var(--blue)"/>
          <stop offset="1" stop-color="var(--blue-deep)"/>
        </linearGradient>
      </defs>
      <rect width="1007" height="599" fill="url(#back-sky)"/>
      <ellipse cx="-210" cy="330" rx="440" ry="560" fill="var(--orange-light)"/>
      <ellipse cx="-240" cy="330" rx="430" ry="560" fill="var(--orange)"/>
    </svg>

    <ul class="social">
      <li class="social__item" style="top:157px"><span class="social__tile"></span><span class="social__handle">briskpelicanmedia</span></li>
      <li class="social__item" style="top:293px"><span class="social__tile"></span><span class="social__handle">briskpelicanmedia</span></li>
      <li class="social__item" style="top:438px"><span class="social__tile"></span><span class="social__handle">briskpelicanmedia</span></li>
    </ul>
  </section>

</main>
</body>
</html>
```